Business card for a gourmet fruit and vegetable retail store

Please design a business card for our boutique gourmet fruit and vegetable food store using attached logo design, with the colour options of white, black and lime green. We would like it to be unique and classic, with a large image of the logo on the back of the business card, and the business card details plus a design on the front.

Target Market(s)

High income earners in an affluent Melbourne suburb who value high quality products and done mind paying for it

Industry/Entity Type

Retail

Contact Information for Business Card

Business name: Harwick's Fine Food Merchant
Address: 27 Plumtree Rd, Kelsby VIC 3158
Name: TBC
Position Title: Director
Phone Number: TBC
Mobile: TBC

Business name is: Harwick's Fine Food Merchant. Please allow space for us to fill in the business address, contact number, person's name, position Title and mobile number.

Colors
acd036

Requirements
Must have
• The logo must have our business logo on the back, and our business details and contact details on the front. It must include the colours of white, black and lime green
Nice to have
• It can have different background colours on the front and on the back.
Should not have
• It should not have any other colours aside from white, black and lime green

```html
<!DOCTYPE html>
<html lang="en">
<head>
<meta charset="utf-8">
<title>Harwick's Fine Food Merchant — Business Card</title>
<link href="https://fonts.googleapis.com/css2?family=Rokkitt:wght@300;400&family=Lato:wght@400&display=swap" rel="stylesheet">
<style>
  :root {
    --lime: #acd036;
    --lime-deep: #9cc21f;
    --ink: #1e1e1e;
    --ink-soft: #3a3a3a;
    --paper: #ffffff;
    --paper-shade: #f1f1f1;
    --stage: #2b2b2b;
  }
  * { margin: 0; padding: 0; box-sizing: border-box; }
  html, body { width: 1200px; height: 900px; overflow: hidden; }
  body {
    background: var(--stage);
    display: flex;
    flex-direction: column;
    align-items: center;
    justify-content: center;
    gap: 56px;
    font-family: "Rokkitt", Georgia, serif;
  }
  .card {
    width: 640px;
    height: 366px;
    border-radius: 22px;
    position: relative;
    overflow: hidden;
  }

  /* Shared name block: plain circle beside the business name */
  .brand-name {
    display: flex;
    align-items: center;
    gap: 14px;
  }
  .brand-name__circle {
    flex: none;
    border-radius: 50%;
  }
  .brand-name__text {
    font-weight: 400;
    line-height: 1.15;
  }

  /* Back of card */
  .card--back {
    background: linear-gradient(135deg, #b9da45 0%, var(--lime) 45%, var(--lime-deep) 100%);
    display: flex;
    align-items: center;
    justify-content: center;
  }
  .card--back .brand-name__circle {
    width: 40px; height: 40px;
    border: 2px solid var(--paper);
  }
  .card--back .brand-name__text {
    color: var(--paper);
    font-size: 34px;
  }

  /* Front of card */
  .card--front {
    background: linear-gradient(160deg, var(--paper) 0%, var(--paper) 60%, var(--paper-shade) 100%);
    color: var(--ink);
  }
  .front__brand {
    position: absolute;
    left: 40px; top: 128px;
    width: 214px;
  }
  .front__brand .brand-name { gap: 10px; }
  .front__brand .brand-name__circle {
    width: 24px; height: 24px;
    border: 2px solid var(--ink);
  }
  .front__brand .brand-name__text {
    color: var(--ink);
    font-size: 21px;
  }
  .front__divider {
    position: absolute;
    left: 272px; top: 70px;
    width: 2px; height: 176px;
    background: var(--lime);
  }
  .contact {
    position: absolute;
    left: 300px; top: 66px;
  }
  .contact__name {
    font-size: 28px;
    font-weight: 400;
    line-height: 1;
    color: var(--ink);
  }
  .contact__title {
    font-family: "Lato", Arial, sans-serif;
    font-size: 16px;
    color: var(--lime-deep);
    margin-top: 4px;
  }
  .contact__list {
    list-style: none;
    margin-top: 18px;
    display: flex;
    flex-direction: column;
    gap: 5px;
  }
  .contact__item {
    display: flex;
    align-items: center;
    gap: 10px;
    font-size: 19px;
    font-weight: 300;
    color: var(--ink-soft);
    line-height: 1;
  }
  .contact__icon { width: 20px; height: 20px; flex: none; }
  .front__address {
    position: absolute;
    left: 0; right: 0; bottom: 40px;
    text-align: center;
    font-size: 20px;
    font-weight: 300;
    color: var(--ink-soft);
  }
</style>
</head>
<body>

  <section class="card card--back" aria-label="Business card, back">
    <div class="brand-name">
      <div class="brand-name__circle"></div>
      <p class="brand-name__text">Harwick's Fine Food Merchant</p>
    </div>
  </section>

  <section class="card card--front" aria-label="Business card, front">
    <div class="front__brand">
      <div class="brand-name">
        <div class="brand-name__circle"></div>
        <p class="brand-name__text">Harwick's<br>Fine Food Merchant</p>
      </div>
    </div>

    <div class="front__divider"></div>

    <div class="contact">
      <h1 class="contact__name">Daniel Marlowe</h1>
      <p class="contact__title">managing director</p>
      <ul class="contact__list">
        <li class="contact__item">
          <svg class="contact__icon" viewBox="0 0 20 20" aria-hidden="true">
            <circle cx="10" cy="10" r="9" fill="none" stroke="#acd036" stroke-width="1.6"/>
            <path d="M5.5 9 Q10 5 14.5 9 L13 11 L11.5 9.8 L8.5 9.8 L7 11 Z" fill="#acd036"/>
          </svg>
          <span>03 9555 0142</span>
        </li>
        <li class="contact__item">
          <svg class="contact__icon" viewBox="0 0 20 20" aria-hidden="true">
            <circle cx="10" cy="10" r="9" fill="none" stroke="#acd036" stroke-width="1.6"/>
            <rect x="7" y="5" width="6" height="10" rx="1.2" fill="none" stroke="#acd036" stroke-width="1.4"/>
            <circle cx="10" cy="13" r="0.8" fill="#acd036"/>
          </svg>
          <span>0412 555 873</span>
        </li>
        <li class="contact__item">
          <svg class="contact__icon" viewBox="0 0 20 20" aria-hidden="true">
            <circle cx="10" cy="10" r="9" fill="#acd036"/>
            <rect x="5.5" y="7" width="9" height="6.5" fill="#fff"/>
            <path d="M5.5 7 L10 10.6 L14.5 7" fill="none" stroke="#acd036" stroke-width="1.1"/>
          </svg>
          <span>d.marlowe@harwickfinefood.com</span>
        </li>
        <li class="contact__item">
          <svg class="contact__icon" viewBox="0 0 20 20" aria-hidden="true">
            <circle cx="10" cy="10" r="9" fill="#acd036"/>
            <circle cx="10" cy="10" r="5" fill="none" stroke="#fff" stroke-width="1.1"/>
            <ellipse cx="10" cy="10" rx="2.2" ry="5" fill="none" stroke="#fff" stroke-width="1"/>
            <line x1="5" y1="10" x2="15" y2="10" stroke="#fff" stroke-width="1"/>
          </svg>
          <span>www.harwickfinefood.com</span>
        </li>
      </ul>
    </div>

    <p class="front__address">27 Plumtree Rd, Kelsby VIC 3158</p>
  </section>

</body>
</html>
```